Spacer for Aerosol design - Breathwell Orbit Spacer

Require outer box design for Spacer for Aerosol inhaler- Pharmaceutical medical device require high ended design and professional as promoting to Doctor and Pharmacies in UK.

Enclosed Design outline and similar products available in market with variations required.

For more info require about design email- info@kelvashealth.co.uk

1) Name of Products and colour variation in product as below

No Product Colour of Device
1 BreathWell Orbit Adult Blue
2 BreathWell Orbit Adult with mask Blue
3 BreathWell Orbit with Child mask Yellow
4 BreathWell Orbit with Infant mask Orange

2) Colour of box variation require with product colour change i.e. blue, yellow and orange (not whole box colour but strip or lining to indicate diff product)
3) Box dimensions 170 X 80 X 80 mm
4) Spacer design (content) need to be on box with different colour with product variance as product with colour

Target Market(s)

UK

Industry/Entity Type

Pharmaceutical

Colors

Designer to choose colors to be used in the design.

Requirements
Must have
• Professional design as promoting as medical device
Nice to have
• variance in design and graphics

```html
<!DOCTYPE html>
<html lang="en">
<head>
<meta charset="utf-8">
<title>Breathwell Orbit Spacer – Box Fronts</title>
<link rel="stylesheet" href="https://fonts.googleapis.com/css2?family=Exo+2:wght@300;600&family=Oswald:wght@300;500&display=swap">
<style>
  :root {
    --canvas: #8a8a8a;
    --box: #2a303b;
    --box-edge: #1f242d;
    --white: #ffffff;
    --soft-white: #e9ecf1;
    --brand-blue: #3a86c8;
    --blue: #0a6fc4;
    --yellow: #e8e437;
    --orange: #e5720d;
  }
  * { box-sizing: border-box; margin: 0; padding: 0; }
  html, body { width: 1200px; height: 1200px; overflow: hidden; }
  body {
    background: var(--canvas);
    position: relative;
    font-family: "Exo 2", sans-serif;
  }
  .range {
    position: absolute;
    left: 56px; top: 296px;
    display: flex;
    gap: 24px;
  }
  .box-front {
    --accent: var(--blue);
    --tab-text: var(--white);
    position: relative;
    width: 250px; height: 574px;
    background: var(--box);
    border-bottom: 6px solid var(--box-edge);
    border-radius: 2px;
    overflow: hidden;
  }
  .box-front.is-yellow { --accent: var(--yellow); --tab-text: #2a2a20; }
  .box-front.is-orange { --accent: var(--orange); }

  .variant-tab {
    position: absolute;
    top: 0; right: 0;
    width: 182px; height: 23px;
    background: var(--accent);
    border-bottom-left-radius: 100% 100%;
    font-family: "Oswald", sans-serif;
    font-weight: 500;
    font-size: 16px;
    line-height: 23px;
    color: var(--tab-text);
    text-align: right;
    padding-right: 32px;
    white-space: nowrap;
  }
  .maker {
    position: absolute;
    top: 408px; right: 32px;
    display: flex; align-items: center; gap: 6px;
    font-weight: 600;
    font-size: 11px;
    letter-spacing: 0.06em;
    color: var(--brand-blue);
    border-bottom: 1px solid var(--brand-blue);
    padding-bottom: 2px;
  }
  .maker { top: 112px; }
  .maker-dot {
    width: 10px; height: 10px;
    border-radius: 50%;
    background: var(--brand-blue);
  }
  .product-name {
    position: absolute;
    top: 140px; right: 32px;
    text-align: right;
    color: var(--white);
    line-height: 1;
  }
  .product-name .line-main { display: block; font-weight: 600; font-size: 29px; }
  .product-name .line-sub { display: block; font-weight: 300; font-size: 22px; margin-top: 1px; }
  .product-type {
    position: absolute;
    top: 198px; right: 32px;
    font-family: "Oswald", sans-serif;
    font-weight: 300;
    font-size: 13px;
    color: var(--soft-white);
  }
  .ray-field {
    position: absolute;
    left: 150px; top: 220px;
    width: 100px; height: 330px;
  }
  .device-photo {
    position: absolute;
    left: 28px; top: 208px;
    width: 128px; height: 332px;
    border-radius: 18px;
    background: linear-gradient(180deg, #4a5aa8 0%, #cfd5e2 22%, #e6e9ef 55%, #cfd5e2 85%, #4a5aa8 100%);
  }
</style>
</head>
<body>
  <main class="range">
    <section class="box-front is-blue">
      <div class="variant-tab">Adult</div>
      <div class="maker"><span class="maker-dot"></span>Kelvas Health</div>
      <h2 class="product-name"><span class="line-main">Breathwell</span><span class="line-sub">Orbit</span></h2>
      <p class="product-type">Spacer Device</p>
      <svg class="ray-field" viewBox="0 0 100 330" role="img" aria-label="Fan of fine light rays in the variant colour">
        <defs><linearGradient id="ray-blue" x1="0" y1="0" x2="0" y2="1"><stop offset="0" stop-color="#0a6fc4" stop-opacity="0.55"/><stop offset="1" stop-color="#0a6fc4" stop-opacity="0.12"/></linearGradient></defs>
        <polygon points="0,150 100,0 100,330 0,200" fill="url(#ray-blue)"/>
      </svg>
      <div class="device-photo" role="img" aria-label="Photograph of the translucent spacer device with blue mouthpiece and base"></div>
    </section>

    <section class="box-front is-blue">
      <div class="variant-tab">Adult with mask</div>
      <div class="maker"><span class="maker-dot"></span>Kelvas Health</div>
      <h2 class="product-name"><span class="line-main">Breathwell</span><span class="line-sub">Orbit</span></h2>
      <p class="product-type">Spacer Device</p>
      <svg class="ray-field" viewBox="0 0 100 330" role="img" aria-label="Fan of fine light rays in the variant colour">
        <defs><linearGradient id="ray-blue2" x1="0" y1="0" x2="0" y2="1"><stop offset="0" stop-color="#0a6fc4" stop-opacity="0.55"/><stop offset="1" stop-color="#0a6fc4" stop-opacity="0.12"/></linearGradient></defs>
        <polygon points="0,150 100,0 100,330 0,200" fill="url(#ray-blue2)"/>
      </svg>
      <div class="device-photo" role="img" aria-label="Photograph of the translucent spacer device with blue mouthpiece and base"></div>
    </section>

    <section class="box-front is-yellow">
      <div class="variant-tab">With child mask</div>
      <div class="maker"><span class="maker-dot"></span>Kelvas Health</div>
      <h2 class="product-name"><span class="line-main">Breathwell</span><span class="line-sub">Orbit</span></h2>
      <p class="product-type">Spacer Device</p>
      <svg class="ray-field" viewBox="0 0 100 330" role="img" aria-label="Fan of fine light rays in the variant colour">
        <defs><linearGradient id="ray-yellow" x1="0" y1="0" x2="0" y2="1"><stop offset="0" stop-color="#e8e437" stop-opacity="0.55"/><stop offset="1" stop-color="#7fc8b8" stop-opacity="0.12"/></linearGradient></defs>
        <polygon points="0,150 100,0 100,330 0,200" fill="url(#ray-yellow)"/>
      </svg>
      <div class="device-photo" role="img" aria-label="Photograph of the translucent spacer device with blue mouthpiece and base"></div>
    </section>

    <section class="box-front is-orange">
      <div class="variant-tab">With infant mask</div>
      <div class="maker"><span class="maker-dot"></span>Kelvas Health</div>
      <h2 class="product-name"><span class="line-main">Breathwell</span><span class="line-sub">Orbit</span></h2>
      <p class="product-type">Spacer Device</p>
      <svg class="ray-field" viewBox="0 0 100 330" role="img" aria-label="Fan of fine light rays in the variant colour">
        <defs><linearGradient id="ray-orange" x1="0" y1="0" x2="0" y2="1"><stop offset="0" stop-color="#e5720d" stop-opacity="0.55"/><stop offset="1" stop-color="#9fb0b8" stop-opacity="0.12"/></linearGradient></defs>
        <polygon points="0,150 100,0 100,330 0,200" fill="url(#ray-orange)"/>
      </svg>
      <div class="device-photo" role="img" aria-label="Photograph of the translucent spacer device with blue mouthpiece and base"></div>
    </section>
  </main>
</body>
</html>
```